Mobile App design improvement- Figma

I have four screens need to redesign, and I have the design guide to help you.
The goal is to make the design clean and easy to understand CTA improve UI/UX. You can change the icons, and don't change the fonts or color. Also, if you are doing a great job, I will hire you finish the rest of the design of the app.
Here is our site: https://pelvosta.com
Pelvosta App is wishlist:
Hight features and app propositions of the app collaborative shopping and chatting with invited friends and family. Easily to get feedback and make decisions of the products from friends, chat, vote, poll, compare.
Here is the Figma link: https://www.example-design.com/design/Kx7Tq2LmWz9PbNv4HdYsRe/Pelvosta--App?node-id=31-47215&t=Jq8WmZr3VxNt5KpLa-7
Here is the app links:
IOS app:
https://lnkhop.io/8KqTz2m

Android app:
https://lnkhop.io/8KqTz2p
Updates

1. I need to have more design ideas that makes users feel simple and easy to understudy platforms can add products from search products, paste url, and use share button to add proton there wishlist from other e-commerce sites. Simplify the search, paste url, and user share button page, maybe combine search with paste url in the search bar, or switch back and forth with search key, paste URL, or share product from other e-commerce sites. Shop page, maybe show users to pick favorites brands recommended products and popular brands. My profile page, I need to be simple but also give users ability to navigate between the save money and wishlists. Please don’t change my color of the app header and color theme. Tone: Ecommerce marketplace, social media, fun! Highlights invite friends chat, save money, and add product.

Target Market(s)

female CEOs, moms, female interns

Industry/Entity Type

Social networking, shopping.

Number of Pages Required

4 page

Font styles to use
Other font styles liked:
• please look at our brand guide

Requirements
Nice to have
• Simple design, highlight invite memebers, and highlight 3 options for them to get products into one place. Highlight collabrative and social tone.
Should not have
• Don't give me too much colors.

```html
<!DOCTYPE html>
<html lang="en">
<head>
<meta charset="utf-8">
<title>Mobile App Design Improvement – Pelvosta App</title>
<link rel="stylesheet" href="https://fonts.googleapis.com/css2?family=Inter:wght@400;500;600;700;800&display=swap">
<style>
  :root{
    --indigo-deep:#1d1670;
    --stage-grey:#dcdcdc;
    --brand:#4a37d0;
    --brand-soft:#b5aef2;
    --brand-tint:#eeedfc;
    --brand-line:#7767e6;
    --ink:#2b2b33;
    --ink-soft:#9a9aa6;
    --white:#ffffff;
    --mint-bg:#ddf6f1;
    --mint-line:#63d2c2;
    --mint-ink:#137a6d;
    --orchid-bg:#f8e3fb;
    --orchid-line:#e48be9;
    --sun:#f4b52c;
    --thanks:#cfcfcf;
  }
  *{box-sizing:border-box;margin:0;padding:0}
  html,body{width:1200px;height:1097px;overflow:hidden}
  body{font-family:"Inter",sans-serif;position:relative;background:var(--stage-grey)}
  .stage-top{position:absolute;left:0;top:0;width:1200px;height:611px;background:var(--indigo-deep)}
  .headline{position:absolute;top:96px;left:0;width:1200px;text-align:center;color:var(--white);font-weight:800;font-size:43px;letter-spacing:.2px}
  .screen-label{position:absolute;top:207px;color:var(--white);font-weight:700;font-size:12.5px;letter-spacing:.3px}
  .screen-label.profile{left:352px}
  .screen-label.finder{left:665px}
  .thanks{position:absolute;top:968px;left:0;width:1200px;text-align:center;color:var(--thanks);font-weight:800;font-size:43px}

  .screen{position:absolute;width:414px;background:var(--white);border-radius:34px;overflow:hidden;transform:scale(.614);transform-origin:0 0}
  .screen.profile{left:262px;top:265px;height:916px}
  .screen.finder{left:634px;top:265px;height:998px}
  .abs{position:absolute}

  .header-band{position:absolute;left:0;top:0;width:414px}
  .status{position:absolute;top:26px;left:15px;right:20px;display:flex;justify-content:space-between;color:var(--white);font-size:13px;font-weight:500}
  .back-btn{position:absolute;left:15px;top:70px;width:28px;height:28px;border-radius:50%;background:rgba(255,255,255,.25);display:flex;align-items:center;justify-content:center}
  .screen-title{position:absolute;top:72px;left:0;width:414px;text-align:center;color:var(--white);font-weight:700;font-size:21px}
  .mini-avatar{position:absolute;right:16px;top:66px;width:38px;height:38px;border-radius:50%;background:var(--sun)}

  .hero-avatar{position:absolute;left:143px;top:120px;width:126px;height:126px;border-radius:50%;background:radial-gradient(circle at 50% 45%,#f7c64c,#eea81c)}
  .user-name{position:absolute;top:258px;width:414px;text-align:center;font-size:16px;color:var(--ink)}
  .user-handle{position:absolute;top:282px;width:414px;text-align:center;font-size:12px;color:#b4b4bc}

  .savings-card{position:absolute;top:312px;width:121px;height:124px;background:var(--brand-tint);border-radius:6px;text-align:center}
  .savings-card .icon{margin:22px auto 0;width:48px;height:48px;border-radius:50%;background:#c9c3f6;border:2px solid var(--brand);display:flex;align-items:center;justify-content:center}
  .savings-card .label{margin-top:16px;font-size:15px;color:#555}
  .savings-card .label.small{font-size:13.5px}

  .tabs{position:absolute;left:15px;top:456px;width:384px;height:38px;display:flex;border:1px solid #e4e4ea;border-radius:4px;overflow:hidden}
  .tab{flex:1;display:flex;align-items:center;justify-content:center;font-size:14.5px;color:#c7c7cf}
  .tab.active{background:var(--brand);color:var(--white);font-weight:500}

  .wish-card{position:absolute;top:510px;width:182px;height:231px;border:1px solid #ebebef;border-radius:4px;overflow:hidden}
  .wish-card .photo{height:170px}
  .wish-card .name{margin:12px 0 0 10px;font-size:14.5px;color:var(--ink);font-weight:500;display:flex;justify-content:space-between;padding-right:10px}
  .wish-card .members{margin:8px 0 0 10px;font-size:13px;color:#8e8e98}

  .tab-bar{position:absolute;left:0;width:414px;height:86px;border-top:1px solid #f0f0f3;display:flex;justify-content:space-around;padding:0 6px}
  .tab-item{display:flex;flex-direction:column;align-items:center;gap:6px;padding-top:18px;font-size:12.5px;color:var(--brand-soft)}
  .tab-item.active{color:var(--brand);font-weight:500}

  .method-card{position:absolute;left:15px;width:384px;border-radius:6px;border:1.5px solid}
  .method-card.search{top:180px;height:193px;background:var(--brand-tint);border-color:var(--brand-line)}
  .method-card.share{top:394px;height:238px;background:var(--mint-bg);border-color:var(--mint-line)}
  .method-card.link{top:652px;height:221px;background:var(--orchid-bg);border-color:var(--orchid-line)}
  .method-art{position:absolute;border-radius:8px}
  .method-title{position:absolute;font-size:16.5px;font-weight:500;line-height:24px}
  .method-desc{position:absolute;font-size:13px;color:#333;line-height:23px}
  .share .method-desc{font-size:12.5px;line-height:24px}
  .field{position:absolute;left:22px;height:45px;background:var(--white);border-radius:6px;display:flex;align-items:center;justify-content:space-between;padding:0 12px 0 15px;font-size:12.5px;color:#444}
  .step{position:absolute;width:60px;height:60px;border-radius:50%;background:var(--white);border:1.5px solid;display:flex;flex-direction:column;align-items:center;justify-content:center;color:#111}
  .step b{font-family:"Inter",sans-serif;font-weight:500;font-size:22px;line-height:22px}
  .step span{font-size:10px;margin-top:2px}
  .share-bar{position:absolute;left:22px;top:176px;width:268px;height:48px;background:var(--white);border-radius:6px;display:flex;justify-content:space-around;align-items:center}
</style>
</head>
<body>
  <div class="stage-top"></div>
  <h1 class="headline">MOBILE APP DESIGN IMPROVEMENT- FIGMA</h1>
  <div class="screen-label profile">MY PROFILE</div>
  <div class="screen-label finder">3 WAY TO FIND PRODUCTS</div>

  <!-- Profile screen -->
  <section class="screen profile">
    <svg class="header-band" width="414" height="180" viewBox="0 0 414 180">
      <path d="M0 0H414V172C370 148 330 160 290 168H124C84 160 44 148 0 172Z" fill="var(--brand)"/>
      <path d="M0 172C44 152 84 160 124 168L124 158C84 150 44 142 0 160Z" fill="#6f60dc"/>
      <path d="M414 172C370 152 330 160 290 168L290 158C330 150 370 142 414 160Z" fill="#6f60dc"/>
    </svg>
    <div class="status"><span>12:30PM</span>
      <svg width="76" height="14" viewBox="0 0 76 14"><g fill="#fff"><rect x="0" y="9" width="3" height="5"/><rect x="5" y="5" width="3" height="9"/><rect x="10" y="1" width="3" height="13"/></g><path d="M26 6a10 10 0 0 1 14 0M29 9a6 6 0 0 1 8 0" stroke="#fff" stroke-width="1.8" fill="none"/><circle cx="33" cy="12" r="1.5" fill="#fff"/><rect x="52" y="2" width="21" height="10" rx="2.5" stroke="#fff" stroke-width="1.5" fill="none"/><rect x="54.5" y="4.5" width="16" height="5" fill="#fff"/></svg>
    </div>
    <div class="back-btn"><svg width="10" height="10" viewBox="0 0 10 10"><path d="M6.5 1.5 3 5l3.5 3.5" stroke="#fff" stroke-width="1.8" fill="none"/></svg></div>
    <div class="screen-title">My Profile</div>
    <div class="mini-avatar" role="img" aria-label="User profile photo"></div>
    <div class="hero-avatar" role="img" aria-label="User profile photo"></div>
    <div class="user-name">Marisol K.</div>
    <div class="user-handle">@marisolk</div>

    <div class="savings-card" style="left:15px">
      <div class="icon"><svg width="26" height="26" viewBox="0 0 26 26"><rect x="6" y="3" width="14" height="20" rx="3" transform="rotate(35 13 13)" stroke="#4a37d0" stroke-width="2" fill="none"/><path d="M10 16 16 10" stroke="#4a37d0" stroke-width="2"/></svg></div>
      <div class="label">1&nbsp; Price drop</div>
    </div>
    <div class="savings-card" style="left:147px">
      <div class="icon"><svg width="28" height="22" viewBox="0 0 28 22"><rect x="2" y="3" width="24" height="16" rx="2" stroke="#4a37d0" stroke-width="2" fill="none"/><circle cx="14" cy="11" r="5" stroke="#4a37d0" stroke-width="1.8" fill="none"/><path d="M11.5 13.5l5-5" stroke="#4a37d0" stroke-width="1.6"/></svg></div>
      <div class="label">0 Coupons</div>
    </div>
    <div class="savings-card" style="left:278px">
      <div class="icon"><svg width="28" height="24" viewBox="0 0 28 24"><rect x="3" y="5" width="22" height="15" rx="1.5" stroke="#4a37d0" stroke-width="2" fill="none"/><rect x="7" y="9" width="14" height="7" stroke="#4a37d0" stroke-width="1.6" fill="none"/><circle cx="14" cy="12.5" r="2" fill="#4a37d0"/></svg></div>
      <div class="label small">Earn Cash Back</div>
    </div>

    <div class="tabs"><div class="tab active">My Wish Lists</div><div class="tab">Joined Wish Lists</div></div>

    <article class="wish-card" style="left:15px">
      <div class="photo" role="img" aria-label="Photo of a gold and chocolate celebration cake" style="background:linear-gradient(160deg,#d9c39a,#6d5637 55%,#3a2d22)"></div>
      <div class="name"><span>Default Wishlist</span><svg width="13" height="16" viewBox="0 0 13 16"><path d="M3 7V5a3.5 3.5 0 0 1 7 0v2" stroke="#4a37d0" stroke-width="2" fill="none"/><rect x="1" y="7" width="11" height="8" rx="1.5" fill="#4a37d0"/></svg></div>
      <div class="members">10 Members</div>
    </article>
    <article class="wish-card" style="left:216px">
      <div class="photo" role="img" aria-label="Photo of a woman in a pink evening gown" style="background:linear-gradient(180deg,#1d3f5e,#2d5a63 50%,#c98a8f)"></div>
      <div class="name"><span>Dress Collection</span></div>
      <div class="members">10 Members</div>
    </article>

    <nav class="tab-bar" style="top:830px">
      <div class="tab-item active"><svg width="26" height="24" viewBox="0 0 26 24"><path d="M3 10 13 2l10 8v11a1 1 0 0 1-1 1H4a1 1 0 0 1-1-1Z" stroke="currentColor" stroke-width="2" fill="none"/><path d="M10 18h6" stroke="currentColor" stroke-width="2"/></svg>Home</div>
      <div class="tab-item"><svg width="26" height="26" viewBox="0 0 26 26"><circle cx="13" cy="13" r="11" stroke="currentColor" stroke-width="2" fill="none"/><path d="M5 8c4 0 5 3 4 6s2 4 2 8M17 3c-1 3 1 5 4 5M15 23c0-3 2-5 5-5" stroke="currentColor" stroke-width="1.6" fill="none"/></svg>Discover</div>
      <div class="tab-item"><svg width="26" height="26" viewBox="0 0 26 26"><path d="M3 4h20v15H15l-2 3-2-3H3Z" stroke="currentColor" stroke-width="2" fill="none"/><path d="M13 16s-5-3-5-6a2.5 2.5 0 0 1 5-1 2.5 2.5 0 0 1 5 1c0 3-5 6-5 6Z" stroke="currentColor" stroke-width="1.6" fill="none"/></svg>Wishlist</div>
      <div class="tab-item"><svg width="28" height="26" viewBox="0 0 28 26"><path d="M8 4h17v13h-3v4l-4-4H8Z" stroke="currentColor" stroke-width="2" fill="none"/><path d="M5 8H3v13l3-3h10" stroke="currentColor" stroke-width="2" fill="none"/><path d="M13 11h1M16 11h1M19 11h1" stroke="currentColor" stroke-width="2"/></svg>Chat</div>
      <div class="tab-item"><svg width="24" height="26" viewBox="0 0 24 26"><rect x="3" y="5" width="18" height="18" rx="2" stroke="currentColor" stroke-width="2" fill="none"/><path d="M8 11a4 4 0 0 0 8 0" stroke="currentColor" stroke-width="2" fill="none"/></svg>Shop</div>
    </nav>
  </section>

  <!-- Find products screen -->
  <section class="screen finder">
    <svg class="header-band" width="414" height="160" viewBox="0 0 414 160">
      <path d="M0 0H414V146C330 128 270 140 207 140S84 128 0 146Z" fill="var(--brand)"/>
      <path d="M0 146C84 128 150 140 207 140S330 128 414 146V136C330 118 270 130 207 130S84 118 0 136Z" fill="#6f60dc"/>
    </svg>
    <div class="status"><span>12:30PM</span>
      <svg width="76" height="14" viewBox="0 0 76 14"><g fill="#fff"><rect x="0" y="9" width="3" height="5"/><rect x="5" y="5" width="3" height="9"/><rect x="10" y="1" width="3" height="13"/></g><path d="M26 6a10 10 0 0 1 14 0M29 9a6 6 0 0 1 8 0" stroke="#fff" stroke-width="1.8" fill="none"/><circle cx="33" cy="12" r="1.5" fill="#fff"/><rect x="52" y="2" width="21" height="10" rx="2.5" stroke="#fff" stroke-width="1.5" fill="none"/><rect x="54.5" y="4.5" width="16" height="5" fill="#fff"/></svg>
    </div>
    <div class="back-btn"><svg width="10" height="10" viewBox="0 0 10 10"><path d="M6.5 1.5 3 5l3.5 3.5" stroke="#fff" stroke-width="1.8" fill="none"/></svg></div>
    <div class="screen-title">3 Way to Find Products</div>
    <div class="mini-avatar" role="img" aria-label="User profile photo"></div>

    <div class="method-card search">
      <div class="method-art" role="img" aria-label="Illustration of a person searching on a laptop" style="left:22px;top:10px;width:110px;height:110px;background:linear-gradient(160deg,#e4e1fb,#b8b0f0)"></div>
      <div class="method-title" style="left:153px;top:26px;color:var(--brand)">Search for Products</div>
      <div class="method-desc" style="left:153px;top:57px">Find products the traditional<br>way with the search bar</div>
      <div class="field" style="top:134px;width:276px">Find what you’re looking for<svg width="15" height="15" viewBox="0 0 15 15"><circle cx="6.5" cy="6.5" r="5" stroke="#aaa" stroke-width="1.4" fill="none"/><path d="m10 10 4 4" stroke="#aaa" stroke-width="1.4"/></svg></div>
      <div class="step" style="left:313px;top:123px;border-color:var(--brand-line)"><b>01</b><span>Step</span></div>
    </div>

    <div class="method-card share">
      <div class="method-art" role="img" aria-label="Illustration of a person sharing products from a phone" style="left:18px;top:20px;width:124px;height:128px;background:linear-gradient(160deg,#d3f1ec,#a9b8ef)"></div>
      <div class="method-title" style="left:166px;top:22px;color:var(--mint-ink)">Save Products From<br>App or Website</div>
      <div class="method-desc" style="left:166px;top:76px">use the share button on other<br>retailer sites or apps to save<br>Items to you Pelvosta wishlist</div>
      <div class="share-bar">
        <svg width="22" height="24" viewBox="0 0 22 24"><path d="M7 9H4v13h14V9h-3M11 15V2M7 6l4-4 4 4" stroke="var(--brand)" stroke-width="2" fill="none"/></svg>
        <svg width="24" height="24" viewBox="0 0 24 24"><circle cx="18" cy="5" r="3" fill="var(--brand)"/><circle cx="6" cy="12" r="3" fill="var(--brand)"/><circle cx="18" cy="19" r="3" fill="var(--brand)"/><path d="M18 5 6 12l12 7" stroke="var(--brand)" stroke-width="2" fill="none"/></svg>
        <svg width="8" height="24" viewBox="0 0 8 24"><circle cx="4" cy="4" r="2.5" fill="var(--brand)"/><circle cx="4" cy="12" r="2.5" fill="var(--brand)"/><circle cx="4" cy="20" r="2.5" fill="var(--brand)"/></svg>
        <svg width="24" height="22" viewBox="0 0 24 22"><path d="M14 2l9 8-9 8v-5C8 13 4 15 1 20c1-8 5-12 13-13Z" fill="var(--brand)"/></svg>
        <svg width="24" height="24" viewBox="0 0 24 24"><path d="M10 4H3v17h17v-7M14 3h7v7M21 3 11 13" stroke="var(--brand)" stroke-width="2" fill="none"/></svg>
      </div>
      <div class="step" style="left:308px;top:166px;border-color:var(--mint-line)"><b>02</b><span>Step</span></div>
    </div>

    <div class="method-card link">
      <div class="method-art" role="img" aria-label="Illustration of a phone with a copied product link" style="left:24px;top:20px;width:112px;height:116px;background:linear-gradient(160deg,#c9c2f6,#6e5fdc)"></div>
      <div class="method-title" style="left:158px;top:40px;color:var(--ink)">Find Product by URL</div>
      <div class="method-desc" style="left:158px;top:71px">Copy and paste product URLs<br>from your favorite online stores</div>
      <div class="field" style="top:161px;width:276px">Paste Product URL<svg width="15" height="15" viewBox="0 0 15 15"><circle cx="6.5" cy="6.5" r="5" stroke="#aaa" stroke-width="1.4" fill="none"/><path d="m10 10 4 4" stroke="#aaa" stroke-width="1.4"/></svg></div>
      <div class="step" style="left:313px;top:143px;border-color:var(--orchid-line)"><b>03</b><span>Step</span></div>
    </div>

    <nav class="tab-bar" style="top:912px">
      <div class="tab-item active"><svg width="26" height="24" viewBox="0 0 26 24"><path d="M3 10 13 2l10 8v11a1 1 0 0 1-1 1H4a1 1 0 0 1-1-1Z" stroke="currentColor" stroke-width="2" fill="none"/><path d="M10 18h6" stroke="currentColor" stroke-width="2"/></svg>Home</div>
      <div class="tab-item"><svg width="26" height="26" viewBox="0 0 26 26"><circle cx="13" cy="13" r="11" stroke="currentColor" stroke-width="2" fill="none"/><path d="M5 8c4 0 5 3 4 6s2 4 2 8M17 3c-1 3 1 5 4 5M15 23c0-3 2-5 5-5" stroke="currentColor" stroke-width="1.6" fill="none"/></svg>Discover</div>
      <div class="tab-item"><svg width="26" height="26" viewBox="0 0 26 26"><path d="M3 4h20v15H15l-2 3-2-3H3Z" stroke="currentColor" stroke-width="2" fill="none"/><path d="M13 16s-5-3-5-6a2.5 2.5 0 0 1 5-1 2.5 2.5 0 0 1 5 1c0 3-5 6-5 6Z" stroke="currentColor" stroke-width="1.6" fill="none"/></svg>Wishlist</div>
      <div class="tab-item"><svg width="28" height="26" viewBox="0 0 28 26"><path d="M8 4h17v13h-3v4l-4-4H8Z" stroke="currentColor" stroke-width="2" fill="none"/><path d="M5 8H3v13l3-3h10" stroke="currentColor" stroke-width="2" fill="none"/><path d="M13 11h1M16 11h1M19 11h1" stroke="currentColor" stroke-width="2"/></svg>Chat</div>
      <div class="tab-item"><svg width="24" height="26" viewBox="0 0 24 26"><rect x="3" y="5" width="18" height="18" rx="2" stroke="currentColor" stroke-width="2" fill="none"/><path d="M8 11a4 4 0 0 0 8 0" stroke="currentColor" stroke-width="2" fill="none"/></svg>Shop</div>
    </nav>
  </section>

  <div class="thanks">THANKS FOR WATCHING MY WORK</div>
</body>
</html>
```